QCRB Property Flyer - For Support Coordinators

Revamping our current brochures and social media posts for our properties. We need a clearer, simpler design that would be designed for Support Coordinators. Attached is our current brochure for reference.

Key details to highlight would include:
- Type of property: Studio Apartments with Psychosocial Disability Support located in Inner West
- Accommodation features
- Services

Our logo is also attached, please make the brochure with similar branding colours and fonts.
Updates

Designs look the same

Sick

Font styles to use
Sans Serif
Other font styles liked:
• Montserrat Light and Montserrat Semi Bold

Colors
0054AA
0677BA
7BADD7
CADEEF
E8F1F8

Requirements
Nice to have
• Please refer to this style guide: https://slides.brelvanto.com/deck/7TkpWmzaQ2eRvB41nLx0YsdHc9JuFgE3KoiVta8Xq5Nw/view?mode=shared

```html
<!DOCTYPE html>
<html lang="en">
<head>
<meta charset="utf-8">
<title>Petersham Studio Apartments Flyer</title>
<link rel="stylesheet" href="https://fonts.googleapis.com/css2?family=Montserrat:wght@400;500;600&family=Open+Sans:wght@600&family=Roboto:wght@400&family=Barlow+Condensed:wght@400;500&display=swap">
<style>
:root{
  --sky:#7db4e8;
  --sky-deep:#5f9bdc;
  --brick:#3b3a3c;
  --band:rgba(20,20,22,.78);
  --accent:#20a6d6;
  --teal:#7fd3c2;
  --ink:#3a3f55;
  --body:#2a2a2a;
  --panel:#efefef;
  --footer:#3f4458;
  --white:#ffffff;
}
*{margin:0;padding:0;box-sizing:border-box}
html,body{width:990px;height:1200px;overflow:hidden;background:#fff}
.flyer{position:relative;width:990px;height:1200px;background:var(--white);font-family:"Roboto",sans-serif;overflow:hidden}
.hero-photo{position:absolute;left:0;top:0;width:990px;height:590px;
  background:linear-gradient(180deg,var(--sky-deep) 0%,var(--sky) 35%,#9cc3e4 55%,#6b6560 70%,var(--brick) 100%)}
.title-frame{position:absolute;left:79px;top:67px;width:832px;height:121px;border:3px solid var(--white);
  display:flex;align-items:center;justify-content:center}
.title-frame h1{font-family:"Montserrat",sans-serif;font-weight:600;font-size:86px;letter-spacing:26px;margin-right:-26px;
  color:#ececec;text-shadow:0 3px 4px rgba(0,0,0,.35)}
.hero-band{position:absolute;left:0;top:457px;width:990px;height:133px;background:var(--band);text-align:center;color:var(--white);
  font-family:"Open Sans",sans-serif;font-weight:600}
.hero-band .line1{font-size:30px;margin-top:22px;line-height:36px}
.hero-band .line2{font-size:28px;line-height:40px}
.address{position:absolute;left:181px;top:567px;width:627px;height:47px;background:var(--accent);color:var(--white);
  display:flex;align-items:center;justify-content:center;gap:10px;font-family:"Montserrat",sans-serif;font-weight:600;font-size:24px}
.welcome{position:absolute;left:78px;top:644px;width:560px}
.welcome h2{font-family:"Montserrat",sans-serif;font-weight:400;font-size:41px;line-height:48px;color:var(--ink);letter-spacing:-.5px;white-space:nowrap}
.welcome h2 span{color:var(--accent);font-weight:600}
.welcome p{font-size:15.2px;line-height:18.5px;color:var(--body);text-align:justify;margin-top:10px}
.welcome p.note{text-align:left;margin-top:10px;font-size:14.6px;letter-spacing:-.2px}
.brand{position:absolute;left:650px;top:668px;width:280px;text-align:center}
.brand .mark{width:86px;height:86px;border-radius:50%;background:var(--accent);margin:0 auto 18px}
.brand .name{font-family:"Montserrat",sans-serif;font-weight:400;font-size:16px;letter-spacing:1.5px;color:var(--ink);white-space:nowrap}
.panel{position:absolute;top:831px;width:402px;height:285px;background:var(--panel)}
.panel.left{left:78px}.panel.right{left:509px}
.panel-head{height:49px;background:var(--accent);color:var(--white);font-family:"Barlow Condensed",sans-serif;font-weight:500;
  font-size:31px;padding-left:46px;line-height:50px;position:relative}
.panel-head::after{content:"";position:absolute;right:0;bottom:0;border-style:solid;border-width:0 0 22px 22px;border-color:transparent transparent var(--teal) transparent}
.panel::after{content:"";position:absolute;right:0;bottom:0;border-style:solid;border-width:26px 26px 0 0;border-color:transparent var(--teal) transparent transparent}
.item{position:absolute;left:56px;height:60px;display:flex;align-items:center;gap:22px}
.item .icon{width:58px;height:58px;border-radius:50%;background:linear-gradient(135deg,#26a7d8,#7fd3c2);border:3px solid #fff;
  box-shadow:-10px 8px 10px rgba(0,0,0,.12);display:flex;align-items:center;justify-content:center;flex:none}
.item p{font-family:"Barlow Condensed",sans-serif;font-size:21px;line-height:30px;color:#222;white-space:nowrap}
.i1{top:64px}.i2{top:134px}.i3{top:205px}
.footer-rule{position:absolute;left:0;top:1142px;width:990px;height:4px;background:linear-gradient(90deg,var(--accent),var(--teal))}
.footer{position:absolute;left:0;top:1146px;width:990px;height:54px;background:var(--footer);color:var(--white);
  display:flex;align-items:center;justify-content:center;gap:14px;font-family:"Barlow Condensed",sans-serif;font-size:18px}
.footer .contact{display:flex;align-items:center;gap:7px}
.footer .sep{opacity:.9}
.dot{width:12px;height:12px;border-radius:50%;background:var(--accent)}
</style>
</head>
<body>
<div class="flyer">
  <div class="hero-photo" role="img" aria-label="Photo of the new dark brick apartment building on a leafy Petersham street under a blue sky"></div>
  <div class="title-frame"><h1>PETERSHAM</h1></div>
  <div class="hero-band">
    <p class="line1">STUDIO APARTMENTS WITH</p>
    <p class="line2">Psychosocial Disability Support&nbsp; located in Inner West</p>
  </div>
  <div class="address">
    <svg width="18" height="26" viewBox="0 0 18 26" fill="none" stroke="#fff" stroke-width="2.4"><circle cx="9" cy="8" r="6"/><path d="M9 14v8"/><path d="M3 23h12"/></svg>
    18 Marlow Lane , Petersham NSW 2049
  </div>

  <section class="welcome">
    <h2>WELCOME TO <span>PETERSHAM</span></h2>
    <p>Located in the heart of Petersham, our new 20 self-contained studio apartments which have a kitchen with fridge, small stove top and microwave. It has a single bed, tv, dining table and bathroom. Some apartments have small balconies, and some have decks overlooking the bustling suburb.</p>
    <p class="note">Situated a 5 minute walk to Petersham Train Station, and other public transport.</p>
  </section>

  <div class="brand"><div class="mark"></div><p class="name">KINDRED HARBOUR CARE</p></div>

  <section class="panel left">
    <h3 class="panel-head">COMMUNITIES &amp; FACILITIES</h3>
    <div class="item i1"><span class="icon"><svg width="28" height="26" viewBox="0 0 28 26" fill="none" stroke="#fff" stroke-width="2"><path d="M3 3h22l2 7H1z"/><path d="M4 10v13h20V10"/><path d="M10 23v-7h8v7"/></svg></span><p>Close to shops,<br>cafes and public transport.</p></div>
    <div class="item i2"><span class="icon"><svg width="26" height="26" viewBox="0 0 26 26" fill="none" stroke="#fff" stroke-width="2"><circle cx="13" cy="13" r="10"/><path d="M13 8v10M8 13h10"/></svg></span><p>Local GP Practice and<br>Dentistry.</p></div>
    <div class="item i3"><span class="icon"><svg width="26" height="26" viewBox="0 0 26 26" fill="none" stroke="#fff" stroke-width="2"><path d="M4 4h18l-9 10z"/><path d="M13 14v8M8 22h10"/></svg></span><p>Commercial Space for<br>Social Enterprise.</p></div>
  </section>

  <section class="panel right">
    <h3 class="panel-head">FEATURES &amp; SERVICES</h3>
    <div class="item i1"><span class="icon"><svg width="26" height="26" viewBox="0 0 26 26" fill="none" stroke="#fff" stroke-width="2"><rect x="4" y="2" width="18" height="22" rx="2"/><rect x="8" y="6" width="10" height="7"/><path d="M9 18h8"/></svg></span><p>24/7 Video-Intercom &amp;<br>on site support.</p></div>
    <div class="item i2"><span class="icon"><svg width="26" height="28" viewBox="0 0 26 28" fill="none" stroke="#fff" stroke-width="2.2"><circle cx="10" cy="4" r="2.2"/><path d="M10 8v9h8l3 6"/><path d="M6 13a7 7 0 1 0 10 8"/></svg></span><p>Disability access<br>walkways &amp; bathroom.</p></div>
    <div class="item i3"><span class="icon"><svg width="26" height="26" viewBox="0 0 26 26" fill="none" stroke="#fff" stroke-width="2"><circle cx="13" cy="8" r="5"/><path d="M4 24c0-6 4-9 9-9s9 3 9 9"/></svg></span><p>Trained &amp; experienced Staff in<br>psychosocial disability.</p></div>
  </section>

  <div class="footer-rule"></div>
  <footer class="footer">
    <span class="contact"><svg width="16" height="16" viewBox="0 0 16 16" fill="none" stroke="#20a6d6" stroke-width="1.4"><circle cx="8" cy="8" r="7"/><ellipse cx="8" cy="8" rx="3" ry="7"/><path d="M1 8h14"/></svg>kindredharbour.com.au</span>
    <span class="sep">|</span>
    <span class="contact"><svg width="18" height="13" viewBox="0 0 18 13" fill="none" stroke="#20a6d6" stroke-width="1.4"><rect x="1" y="1" width="16" height="11"/><path d="M1 1l8 6 8-6"/></svg>info@kindredharbour.com.au</span>
    <span class="sep">|</span>
    <span class="contact"><svg width="16" height="16" viewBox="0 0 16 16" fill="none" stroke="#20a6d6" stroke-width="1.4"><circle cx="8" cy="8" r="7"/><path d="M5 4l2 2-1 1.5c.7 1.3 1.5 2.1 2.5 2.5L10 9l2 2-1.5 1.5C7 12 4 9 3.5 5.5z"/></svg>1300 582 917</span>
    <span class="sep">|</span>
    <span class="contact"><span class="dot"></span>kindredharbour_living</span>
  </footer>
</div>
</body>
</html>
```